Fun relaxed Travel Photography Business Card*

Require a fun, funky and quirky but rememberable business card for a travel photographer

Industry/Entity Type

Photographer

Contact Information for Business Card

Front Card

(my name) Tavo M.

Travel Photographer ( small under travel photographer) “self-proclaimed”

(website logo) wanderingtavo.example

(Instagram logo) @wandering_with_tavo

(Instagram logo) @wandering_with_tavo_2.0 (backup for when Instagram puts Tavo on timeout for bad behaviour)

Tel: N/A (removing the potential awkwardness of me not replying)

Email: (see above)

Back Card

Offending people since 1986

(Bottom right corner) “p.s. travelling made me fatTER”

Font styles to use
Serif

Colors

Designer to choose colors to be used in the design.

Requirements
Must have
• a camera
• a similar cartoon version of me as the "logo" see attached files, try to make as similar as possible

```html
<!DOCTYPE html>
<html lang="en">
<head>
<meta charset="utf-8">
<title>Tavo M. — Travel Photographer Business Card</title>
<link href="https://fonts.googleapis.com/css2?family=Montserrat:wght@400;500;700&display=swap" rel="stylesheet">
<style>
  :root {
    --backdrop: #2b2e34;
    --card-white: #ffffff;
    --brand-blue: #3d628e;
    --brand-blue-light: #4b74a3;
    --ink-grey: #6a6a6a;
    --line-blue: #3d628e;
    --art-navy: #2c3f6e;
    --art-orange: #e0823a;
  }
  * { box-sizing: border-box; margin: 0; padding: 0; }
  html, body {
    width: 1200px; height: 900px; overflow: hidden;
    background: var(--backdrop);
    font-family: "Montserrat", Arial, sans-serif;
  }
  .stage {
    position: relative; width: 1200px; height: 900px;
    display: flex; flex-direction: column; align-items: center; justify-content: center; gap: 60px;
  }
  .card {
    position: relative; width: 560px; height: 320px; overflow: hidden;
    box-shadow: 0 12px 30px rgba(0,0,0,.45);
  }

  /* Front */
  .card--front { background: var(--card-white); }
  .card--front .edge-bar {
    position: absolute; left: 0; bottom: 0; width: 10px; height: 120px; background: var(--brand-blue);
  }
  .card--front .character-art {
    position: absolute; left: 40px; top: 22px; width: 170px; height: 160px; border-radius: 22px;
    background: linear-gradient(135deg, var(--brand-blue) 0%, var(--art-navy) 55%, var(--art-orange) 100%);
  }
  .identity {
    position: absolute; left: 236px; top: 146px; right: 16px;
  }
  .identity .name-line {
    display: flex; align-items: baseline; gap: 8px; color: var(--brand-blue); white-space: nowrap;
  }
  .identity .name { font-size: 26px; font-weight: 700; }
  .identity .divider { font-size: 26px; font-weight: 400; }
  .identity .role { font-size: 14px; font-weight: 700; }
  .identity .tagline { font-size: 12px; color: var(--ink-grey); margin-top: -2px; }

  .contacts {
    position: absolute; left: 224px; top: 200px;
    border-left: 2px solid var(--line-blue); padding-left: 12px;
    list-style: none;
  }
  .contacts li {
    display: flex; align-items: center; gap: 8px;
    font-size: 17px; color: var(--ink-grey); line-height: 24px; white-space: nowrap;
  }
  .contacts .marker {
    width: 13px; height: 13px; background: var(--brand-blue); flex: none;
  }
  .contacts .marker--round { border-radius: 50%; }

  /* Back */
  .card--back {
    background: linear-gradient(160deg, var(--brand-blue) 0%, var(--brand-blue-light) 100%);
  }
  .card--back .band {
    position: absolute; left: 0; right: 0; top: 160px; height: 56px; background: var(--card-white);
  }
  .card--back .character-art {
    position: absolute; left: 320px; top: 36px; width: 170px; height: 170px; border-radius: 22px;
    background: linear-gradient(135deg, #e9eef5 0%, var(--art-navy) 60%, var(--art-orange) 100%);
  }
  .card--back .motto {
    position: absolute; left: 30px; top: 176px;
    font-size: 19px; line-height: 24px; color: var(--brand-blue); font-weight: 400;
  }
  .card--back .postscript {
    position: absolute; left: 40px; top: 232px;
    font-size: 17px; color: var(--card-white);
  }
</style>
</head>
<body>
<main class="stage">
  <section class="card card--front" aria-label="Front of business card">
    <div class="edge-bar"></div>
    <div class="character-art" role="img" aria-label="Illustration area for a cartoon travel-photographer character"></div>
    <div class="identity">
      <div class="name-line">
        <span class="name">Tavo M.</span><span class="divider">|</span><span class="role">Travel Photographer</span>
      </div>
      <p class="tagline">self-proclaimed</p>
    </div>
    <ul class="contacts">
      <li><span class="marker"></span>@wandering_with_tavo</li>
      <li><span class="marker"></span>@wandering_with_tavo_2.0</li>
      <li><span class="marker"></span>tavos.wandering@example.com</li>
      <li><span class="marker marker--round"></span>www.wanderingtavo.example</li>
    </ul>
  </section>

  <section class="card card--back" aria-label="Back of business card">
    <div class="band"></div>
    <div class="character-art" role="img" aria-label="Illustration area for a cartoon travel-photographer character"></div>
    <p class="motto">Offending people since 1986</p>
    <p class="postscript">p.s. travelling made me fatTER</p>
  </section>
</main>
</body>
</html>
```